Hallo liebe Designer,
wir haben bereits ein Design, welches sich an den Farben unserer Homepage www.lorta.de orientiert. Dieses Design muss nachgebaut werden. Wir benötigen eine editierbare Microsoft-WORD-Datei, die nach Bedarf angepasst werden kann (falls sich Telefonnummer oder ähnliches mal ändert)
Zusammengefasst:
Benötigt wird: Ein Worddokument mit einem Briefpapier mit der Hauptseite und Folgeseiten. Die Folgeseiten sollen automatisch entstehen, wenn mehr wie 1 Seite beschrieben wird.
Das Design bitte so nachbauen wie es im PDF ersichtlich ist.
- das Worddokument muss anpassbar sein, falls sich mal die Telefonnummer o.ä. ändert

```html
<!DOCTYPE html>
<html lang="de">
<head>
<meta charset="utf-8">
<title>LOR Unternehmensgruppe – Briefpapier</title>
<link href="https://fonts.googleapis.com/css2?family=Poppins:wght@400;500;600&display=swap" rel="stylesheet">
<style>
  :root {
    --bg: #f1f1f1;
    --paper: #ffffff;
    --green-light: #93ab9e;
    --green-dark: #6b8173;
    --text: #6b7a72;
    --text-strong: #56645c;
  }
  * { margin: 0; padding: 0; box-sizing: border-box; }
  html, body { width: 1200px; height: 1200px; overflow: hidden; background: var(--bg); }
  body { position: relative; font-family: "Poppins", sans-serif; color: var(--text); }

  .sheet {
    position: absolute; top: 215px; width: 540px; height: 769px;
    background: var(--paper); overflow: hidden;
    box-shadow: 6px 6px 10px rgba(0,0,0,0.35);
  }
  .sheet--first { left: 37px; }
  .sheet--following { left: 623px; }

  .brand {
    position: absolute; right: 12px; top: 42px;
    display: flex; align-items: center; gap: 8px;
    color: var(--green-light); font-weight: 500;
  }
  .brand__dot { width: 40px; height: 40px; border-radius: 50%; background: var(--green-dark); }
  .brand__name { font-size: 22px; line-height: 1.15; }
  .brand__name small { display: block; font-size: 12px; }

  .sender-line {
    position: absolute; left: 34px; top: 122px;
    font-size: 7.4px; font-weight: 500; color: var(--text-strong);
  }

  .footer-info {
    position: absolute; left: 34px; top: 685px;
    display: flex; align-items: flex-start;
    font-weight: 500; font-size: 6.2px; line-height: 1.42; color: var(--text-strong);
  }
  .footer-info__col { padding-right: 12px; }
  .footer-info__col--management { width: 110px; }
  .footer-info__col--bank { width: 127px; padding-left: 14px; border-left: 1px solid var(--green-dark); }
  .footer-info__col--contact {
    padding-left: 8px; border-left: 1px solid var(--green-dark);
    font-weight: 400; font-size: 8.4px; line-height: 1.25;
  }
  .footer-info .strong { font-size: 7.2px; font-weight: 600; }
  .footer-info .tiny { font-size: 5.2px; }
  .contact-row { display: flex; align-items: center; gap: 6px; font-size: 7px; }
  .contact-row svg { width: 7px; height: 7px; }

  .band { position: absolute; left: 0; bottom: 0; width: 100%; height: 20px; background: var(--green-light); }
  .band-accent { position: absolute; right: 0; bottom: 0; width: 183px; height: 39px; }
  .web-address {
    position: absolute; right: 38px; bottom: 14px;
    color: #ffffff; font-size: 13.5px; font-weight: 400;
    font-family: "Poppins", sans-serif;
  }
</style>
</head>
<body>

<!-- Erste Seite -->
<section class="sheet sheet--first">
  <div class="brand">
    <span class="brand__dot"></span>
    <div class="brand__name">LOR<small>Unternehmensgruppe</small></div>
  </div>
  <div class="footer-info">
    <div class="footer-info__col footer-info__col--management">
      Geschäftsführung:<br>Markus Fellner<br>Carina Wendt<br>Amtsgericht Lindenau<br><span class="strong">HRB 48107</span>
    </div>
    <div class="footer-info__col footer-info__col--bank">
      Umsatzsteuer-ID<br>DE512840736<br>BIC: NORDDEFFXXX<br>Sparkasse Rheinfeld<br>BIC: RHEFDEDDXXX<br><span class="tiny">IBAN: DE12 3400 0220 4410 6321 58</span>
    </div>
    <div class="footer-info__col footer-info__col--contact">
      Postanschrift:<br>Am Lindenhang<br>41460 Talheim
      <div class="contact-row"><svg viewBox="0 0 10 10"><path d="M2 1l2 2-1 1.5a6 6 0 0 0 2.5 2.5L7 6l2 2-1.5 1.5C4 9 1 6 .5 2.5z" fill="#56645c"/></svg>+49 211 / 45061230</div>
      <div class="contact-row"><svg viewBox="0 0 10 10"><rect x=".5" y="2" width="9" height="6" fill="none" stroke="#56645c" stroke-width=".8"/><path d="M.5 2L5 5.5 9.5 2" fill="none" stroke="#56645c" stroke-width=".8"/></svg>info@lorta.de</div>
    </div>
  </div>
  <div class="band"></div>
  <svg class="band-accent" viewBox="0 0 183 39" preserveAspectRatio="none"><polygon points="21,0 183,0 183,39 0,39" fill="var(--green-dark)"/></svg>
  <div class="web-address">www.lorta.de</div>
</section>

<!-- Folgeseite -->
<section class="sheet sheet--following">
  <div class="brand">
    <span class="brand__dot"></span>
    <div class="brand__name">LOR<small>Unternehmensgruppe</small></div>
  </div>
  <p class="sender-line">LOR Unternehmensgruppe GmbH, Weinbergstraße 72, 63500 Lindenau</p>
  <div class="footer-info">
    <div class="footer-info__col footer-info__col--management">
      Geschäftsführung:<br>Markus Fellner<br>Carina Wendt<br>Amtsgericht Lindenau<br><span class="strong">HRB 48107</span>
    </div>
    <div class="footer-info__col footer-info__col--bank">
      Umsatzsteuer-ID<br>DE512840736<br>BIC: NORDDEFFXXX<br>Sparkasse Rheinfeld<br>BIC: RHEFDEDDXXX<br><span class="tiny">IBAN: DE12 3400 0220 4410 6321 58</span>
    </div>
    <div class="footer-info__col footer-info__col--contact">
      Postanschrift:<br>Am Lindenhang<br>41460 Talheim
      <div class="contact-row"><svg viewBox="0 0 10 10"><path d="M2 1l2 2-1 1.5a6 6 0 0 0 2.5 2.5L7 6l2 2-1.5 1.5C4 9 1 6 .5 2.5z" fill="#56645c"/></svg>+49 211 / 45061230</div>
      <div class="contact-row"><svg viewBox="0 0 10 10"><rect x=".5" y="2" width="9" height="6" fill="none" stroke="#56645c" stroke-width=".8"/><path d="M.5 2L5 5.5 9.5 2" fill="none" stroke="#56645c" stroke-width=".8"/></svg>info@lorta.de</div>
    </div>
  </div>
  <div class="band"></div>
  <svg class="band-accent" viewBox="0 0 183 39" preserveAspectRatio="none"><polygon points="21,0 183,0 183,39 0,39" fill="var(--green-dark)"/></svg>
  <div class="web-address">www.lorta.de</div>
</section>

</body>
</html>
```